Web Design Project

Create a web design

Target Market(s)

Upper class people interested in health

Requirements
Must have
• Templates
Nice to have
• Use the logo provided

```html
<!DOCTYPE html>
<html lang="en">
<head>
<meta charset="utf-8">
<title>Veridian Fitness</title>
<link rel="stylesheet" href="https://fonts.googleapis.com/css2?family=Open+Sans:wght@400;600&display=swap">
<style>
  :root {
    --band-green: rgba(150, 225, 140, 0.85);
    --band-line: #e9f8e4;
    --panel: rgba(14, 44, 14, 0.86);
    --text-light: #ffffff;
    --accent-green: #8fe08f;
    --button-green: #8fe08f;
    --ink: #111a11;
    --dot-blue: #1e73c8;
    --dot-white: #ffffff;
  }
  * { box-sizing: border-box; margin: 0; padding: 0; }
  html, body { width: 1200px; height: 918px; overflow: hidden; }
  body { font-family: "Open Sans", Arial, sans-serif; background: #dfe6dc; }

  .page { position: relative; width: 1200px; height: 918px; overflow: hidden; }

  .hero-photo {
    position: absolute; inset: 0;
    background:
      radial-gradient(ellipse at 50% 28%, rgba(255,255,255,0.75), rgba(255,255,255,0) 55%),
      linear-gradient(180deg, #eef3ee 0%, #dfe9df 22%, #c9d6c4 45%, #a9a88a 70%, #9c8a62 100%);
  }

  .top-band {
    position: absolute; left: 0; top: 43px; width: 1200px; height: 77px;
    background: var(--band-green);
    border-top: 3px solid var(--band-line);
    border-bottom: 3px solid var(--band-line);
  }
  .brand {
    position: absolute; left: 95px; top: 43px; width: 272px; height: 77px;
    background: #ffffff;
    display: flex; align-items: center; justify-content: center;
  }
  .brand-name { font-size: 27px; font-weight: 600; color: var(--ink); white-space: nowrap; }

  .main-nav {
    position: absolute; top: 72px; left: 430px;
    display: flex;
  }
  .main-nav a {
    font-size: 15.5px; color: var(--ink); text-decoration: none;
    margin-right: 20px; white-space: nowrap;
  }
  .main-nav a.is-active { color: var(--text-light); }

  .content-panel {
    position: absolute; left: 98px; top: 327px; width: 1003px; height: 501px;
    background: var(--panel);
  }
  .column { position: absolute; top: 30px; width: 440px; color: var(--text-light); }
  .column-about { left: 40px; }
  .column-packages { left: 522px; }
  .column h2 { font-size: 21px; font-weight: 400; margin-bottom: 10px; }
  .column p { font-size: 18.5px; line-height: 35px; text-align: justify; }
  .package-title { font-size: 18.5px; line-height: 35px; font-weight: 400; color: var(--accent-green); margin-left: 2px; }
  .package + .package { margin-top: 17px; }
  .package p { margin-left: 2px; width: 425px; }

  .more-button {
    position: absolute; top: 435px; width: 82px; height: 40px;
    background: var(--button-green);
    border: 2px solid #ffffff; border-radius: 4px;
    color: var(--ink); font-size: 18px; font-weight: 600;
    display: flex; align-items: center; justify-content: center;
  }
  .more-about { left: 40px; }
  .more-packages { left: 522px; }

  .site-footer { position: absolute; left: 0; top: 860px; width: 1200px; height: 30px; }
  .slider-dots { position: absolute; left: 125px; top: 5px; display: flex; gap: 7px; }
  .slider-dots span { width: 21px; height: 21px; border-radius: 4px; background: var(--dot-white); }
  .slider-dots span.is-current { background: var(--dot-blue); }
  .copyright { position: absolute; left: 247px; top: 6px; font-size: 14px; color: var(--ink); }
  .copyright a { color: var(--ink); }
  .social { position: absolute; left: 881px; top: 2px; display: flex; align-items: center; }
  .social-label { font-size: 14px; color: var(--ink); margin-right: 10px; }
  .social-link { width: 29px; height: 29px; border-radius: 5px; background: #ffffff; border: 2px solid #7fa9d8; margin-right: 9px; }
</style>
</head>
<body>
<div class="page">
  <div class="hero-photo" role="img" aria-label="Bright gym interior with people doing a group stretching class"></div>

  <div class="top-band"></div>
  <div class="brand">
    <span class="brand-name">Veridian Fitness</span>
  </div>
  <nav class="main-nav">
    <a href="#">HOME</a>
    <a href="#" class="is-active">ABOUT US</a>
    <a href="#">SERVICES</a>
    <a href="#">CLIENTS</a>
    <a href="#">PACKAGES</a>
    <a href="#">GET FREE TRIAL FORM</a>
    <a href="#">CONTACT US</a>
  </nav>

  <section class="content-panel">
    <div class="column column-about">
      <h2>ABOUT US</h2>
      <p>We need a web design for a new company based in Harbourvale called "Veridian PT (Personal Training). We are a fitness company that does personal fitness, group fitness and corporate fitness classes. Our initial product is personal training. We would like to see our designs use the colours blue and green (blue for water and green for nature).</p>
      <p>The final design should communicate health and fitness.</p>
    </div>
    <div class="column column-packages">
      <h2>OUR PACKAGES</h2>
      <div class="package">
        <h3 class="package-title">Packages headline1</h3>
        <p>Write here something abour your special packages that you offer.</p>
      </div>
      <div class="package">
        <h3 class="package-title">Packages headline2</h3>
        <p>Write here something abour your special packages that you offer.</p>
      </div>
      <div class="package">
        <h3 class="package-title">Packages headline3</h3>
        <p>Write here something abour your special packages that you offer.</p>
      </div>
    </div>
    <a class="more-button more-about">More</a>
    <a class="more-button more-packages">More</a>
  </section>

  <footer class="site-footer">
    <div class="slider-dots">
      <span class="is-current"></span><span></span><span></span><span></span>
    </div>
    <p class="copyright">Copyright @ 2012, <a href="#">Terms &amp; Privacy Policy</a></p>
    <div class="social">
      <span class="social-label">Follow us :</span>
      <a class="social-link" href="#" aria-label="Social profile one"></a>
      <a class="social-link" href="#" aria-label="Social profile two"></a>
      <a class="social-link" href="#" aria-label="Video channel"></a>
    </div>
  </footer>
</div>
</body>
</html>
```